Corrimbel Lodge Web Design Project

I am looking for a striking, modern and user friendly site to promote my business, Corrimbel Lodge.

Corrimbel Lodge comprises of 3 elements : Restaurant, Resort and Events and the site must showcase all of these.
Updates

Project Deadline Extended
Reason: Too far away from brief ! Please check out the 2 website links to restaurant sites i LOVE for inspiration ! I am happy to pay for a quality designer and also for anyone that can code this !

Target Market(s)

Our Restaurant clientele demographic is 30-60 years old and are a mix of locals and tourists. The Restaurant is very much a destination venue so we attract people that wish to seek out amazing food.

The Event side of things attracts mainly weddings, this is a lucrative arm of the business and this side of the site must also be outstanding.

The Resort comprises of 7 boutique loft apartment and has a big pool and spa. We attract a mix of locals but want to push it as a ' getaway '

Industry/Entity Type

Business

Requirements
Must have
• I would like the first page to be an overall blog and to highlight the 3 area of the business. Lets have the 3 keywords as clickable tabs that take you to that section of the site.

RESTAURANT RESORT EVENTS

The RESTAURANT page should include the following tabs ( i have provided the information to be added to each tab as an example )

MENU ( Breakfast, Lunch, Dinner, Set Menu, Wine List)

FUNCTIONS (Private Dining Room, Exclusive Use, Wine Nights Coming Soon)

RESERVATIONS (Enquiry Form linked to my info@ address, Reservation Policies, Contact Number)

GALLERY & PRESS ( Press Articles, Latest News, What's On, Photo's, Wedding Hot Spot)

CONTACT US (Opening Times, Map, Contact Details, Sign Up For Our Newsletter, Facebook Link )

The RESORT page should include the following tabs :
# LOFTS & RATES
# FACILITIES
# SPECIAL OFFERS
# GALLERY
# RESERVATIONS

The EVENTS page should include the following tabs :
# WEDDINGS
# CONFERENCES
# PRIVATE EVENTS
# GALLERY
# ENQUIRY FORM
Nice to have
• Include Logo, good branding

```html
<!DOCTYPE html>
<html lang="en">
<head>
<meta charset="utf-8">
<title>Corrimbel Lodge</title>
<link href="https://fonts.googleapis.com/css2?family=Questrial&family=Cinzel:wght@400;600&family=Open+Sans:wght@400;600&display=swap" rel="stylesheet">
<style>
:root{
  --orange:#fb5a12;
  --orange-soft:#f36b2a;
  --olive:#6f6a3d;
  --olive-light:#9b9878;
  --sage:#c9c7a8;
  --grey-bg:#efeeee;
  --ink:#3a3a3a;
  --muted:#6b6b6b;
  --white:#ffffff;
}
*{margin:0;padding:0;box-sizing:border-box}
html,body{width:833px;height:1200px;overflow:hidden;background:var(--white)}
body{position:relative;font-family:"Questrial",sans-serif;color:var(--ink)}
.abs{position:absolute}
.top-strip{left:0;top:0;width:833px;height:5px;background:var(--orange)}
.header{left:0;top:5px;width:833px;height:89px;background:var(--white);box-shadow:0 3px 4px rgba(0,0,0,.12);z-index:2}
.brand{left:88px;top:0;width:112px;height:89px;background:var(--orange);display:flex;flex-direction:column;align-items:center;justify-content:center;gap:8px}
.brand-mark{width:26px;height:26px;border:2px solid var(--white)}
.brand-name{font-size:10px;color:var(--white)}
.nav{left:232px;top:0;height:89px;display:flex}
.nav-item{height:89px;display:flex;align-items:center;justify-content:center;font-size:13px;color:#555;border-right:1px solid #e6e6e6;position:relative}
.nav-item.active{color:var(--orange)}
.nav-item.open::after{content:"";position:absolute;left:14px;right:14px;bottom:0;height:5px;background:var(--olive)}
.hero{top:102px;height:216px}
.hero-food{left:0;width:281px;background:linear-gradient(135deg,#8a5a2a,#c8672b 45%,#e2a850 70%,#6d3d1c)}
.hero-pool{left:281px;width:275px;background:linear-gradient(160deg,#7fc7dd,#4aa5c9 45%,#8c7458 60%,#efeeea 80%,#5a4633)}
.hero-dish{left:556px;width:277px;background:linear-gradient(200deg,#2f7d1f,#6ea63b 30%,#e8d9b0 55%,#e45a2c 80%,#f1e2c2)}
.dropdown{left:332px;top:100px;width:61px;height:110px;background:var(--orange-soft);z-index:3;padding:14px 0 0 8px}
.dropdown li{list-style:none;font-family:"Open Sans",sans-serif;font-size:9px;color:var(--white);height:24.5px}
.notch{left:413px;top:300px}
.promo{left:0;top:321px;width:833px;height:57px;background:var(--orange);display:flex;align-items:center;padding-left:145px;gap:14px;color:var(--white)}
.promo-figure{font-size:40px;font-weight:400;letter-spacing:1px}
.promo-text{font-family:"Cinzel",serif;font-size:16px;letter-spacing:1px;margin-top:10px}
.feature{top:378px;height:193px}
.feature-pool{left:0;width:264px;background:linear-gradient(160deg,#d9d8c6,#b6b397 60%,#a19e80)}
.feature-restaurant{left:264px;width:298px;background:var(--white);border-bottom:3px solid var(--orange)}
.feature-restaurant .art{position:absolute;left:40px;top:8px;width:200px;height:178px;border-radius:4px;background:radial-gradient(ellipse at 55% 45%,#efe7db,#d9c4a9 60%,#ffffff 75%)}
.feature-events{left:562px;width:271px;background:linear-gradient(200deg,#c8c6a6,#a8a683 60%,#8f8c6c)}
.feature-label{font-size:16px;line-height:19px;color:var(--white)}
.grid-band{left:0;top:571px;width:833px;height:295px;background:var(--grey-bg)}
.card{top:587px;height:279px}
.about{left:87px;width:172px;background:var(--olive);color:var(--white)}
.offers{left:594px;width:174px;background:var(--olive-light);color:var(--white)}
.card-head{height:42px;border-bottom:1px solid rgba(255,255,255,.6);font-size:16px;padding:15px 0 0 18px}
.card-body{font-size:12.5px;line-height:14.7px;padding:8px 10px 0 12px}
.tasting{background:var(--white);padding:18px 12px 0 12px}
.tasting h3{font-weight:400;font-size:15px;color:#111;margin-bottom:14px}
.tasting h4{font-weight:400;font-size:12.5px;color:#111;margin-bottom:14px}
.tasting p{font-size:12.5px;line-height:14.7px;color:var(--muted)}
.tasting-a{left:259px;top:587px;width:168px;height:140px}
.tasting-b{left:427px;top:726px;width:167px;height:140px}
.photo-pizza{left:427px;top:587px;width:167px;height:139px;background:radial-gradient(circle at 50% 55%,#e7b35c,#c5622a 45%,#6b5a4a 70%,#3e3a36)}
.photo-slice{left:259px;top:727px;width:168px;height:139px;background:linear-gradient(160deg,#6c2a1a,#d9a04a 45%,#f1d28a 60%,#8f5a2c)}
.tri-down{width:0;height:0;border-left:8px solid transparent;border-right:8px solid transparent;border-top:8px solid var(--white)}
.tri-up{width:0;height:0;border-left:8px solid transparent;border-right:8px solid transparent;border-bottom:8px solid var(--white)}
.story{left:0;top:866px;width:833px;height:169px;background:var(--white)}
.story-divider{left:472px;top:866px;width:1px;height:169px;background:#e2e2e2}
.corner{width:22px;height:22px}
.corner.tl{border-top:2px solid var(--orange);border-left:2px solid var(--orange)}
.corner.br{border-bottom:2px solid #222;border-right:2px solid #222}
.produce{left:134px;top:889px;width:91px;height:124px;background:radial-gradient(ellipse at 50% 55%,#8a9a3a,#c24a2a 45%,#e8e2d6 75%,#f6f4f0)}
.newsprint{left:502px;top:926px;width:80px;height:56px;background:linear-gradient(160deg,#f4f4f2,#cfcfcc 55%,#9a9a98)}
.section-title{font-family:"Cinzel",serif;font-size:14px;color:var(--orange);letter-spacing:.5px}
.quote{font-family:"Open Sans",sans-serif;font-size:8.5px;line-height:12px;color:#444}
.link{font-family:"Cinzel",serif;font-size:9px;color:#333;letter-spacing:.5px}
.footer{left:0;top:1035px;width:833px;height:147px;background:var(--grey-bg)}
.foot-head{font-family:"Cinzel",serif;font-size:9px;color:#222;letter-spacing:.5px}
.foot-list li{list-style:none;font-family:"Open Sans",sans-serif;font-size:7px;color:#444;height:14px}
.foot-text{font-family:"Open Sans",sans-serif;font-size:7px;line-height:9px;color:#555}
.bottom-bar{left:0;top:1182px;width:833px;height:18px;background:var(--orange)}
.copyright{left:0;width:833px;top:4px;text-align:center;font-family:"Open Sans",sans-serif;font-size:7px;color:var(--white)}
.social{top:4px;width:10px;height:10px}
</style>
</head>
<body>
<div class="abs top-strip"></div>

<header class="abs header">
  <div class="abs brand"><span class="brand-mark"></span><span class="brand-name">Corrimbel Lodge</span></div>
  <nav class="abs nav">
    <div class="nav-item active" style="width:85px">HOME</div>
    <div class="nav-item open" style="width:90px">MENU</div>
    <div class="nav-item" style="width:100px">FUNCTIONS</div>
    <div class="nav-item" style="width:96px">RESERVATIONS</div>
    <div class="nav-item" style="width:81px">GALLERY</div>
    <div class="nav-item" style="width:88px;border-right:none">CONTACT US</div>
  </nav>
</header>

<div class="abs hero hero-food" role="img" aria-label="Pizza with fresh vegetables, spices and ingredients"></div>
<div class="abs hero hero-pool" role="img" aria-label="Poolside lounger with folded towels"></div>
<div class="abs hero hero-dish" role="img" aria-label="Close-up of a baked dish with basil and tomato"></div>
<ul class="abs dropdown"><li>Breakfast</li><li>Lunch</li><li>Dinner</li><li>Set Menu</li></ul>
<svg class="abs notch" width="30" height="18" viewBox="0 0 30 18"><polygon points="0,18 15,2 30,18" fill="#ffffff"/></svg>

<section class="abs promo">
  <span class="promo-figure">10%</span>
  <span class="promo-text">DICOUNT IN OUR NEW BRANCH</span>
</section>

<div class="abs feature feature-pool" role="img" aria-label="Illustration of a pool cleaner at work by the pool">
  <div class="abs feature-label" style="left:143px;top:32px">ENJOY<br>NICE POOL</div>
</div>
<div class="abs feature feature-restaurant">
  <div class="art" role="img" aria-label="Illustration of a chef carrying a serving dish"></div>
  <div class="abs feature-label" style="right:188px;top:136px;text-align:right;color:#222">BEST</div>
  <div class="abs feature-label" style="left:16px;top:156px;color:var(--orange)">RESTURANT</div>
</div>
<div class="abs feature feature-events" role="img" aria-label="Illustration of a drummer performing at an event">
  <div class="abs feature-label" style="right:12px;top:166px;font-size:19px">events</div>
</div>

<div class="abs grid-band"></div>
<article class="abs card about">
  <div class="card-head">About us</div>
  <p class="card-body">Dummy data is benign information that does not contain any useful data, but serves to re-serve space where real data is nominally pre-sent. Dummy data can be used as cholder for both not contain any useful data, but serves to reserve space where real data is nominally present. Dummy data can be used as cholder for both &nbsp;testing .</p>
</article>
<article class="abs tasting tasting-a">
  <h3>BEST TASTING EVER</h3>
  <p>benign information that does not contain any usefubenign information that does not contain any usefu</p>
</article>
<div class="abs photo-pizza" role="img" aria-label="Whole pizza on a serving board"></div>
<div class="abs photo-slice" role="img" aria-label="Slice of pizza with melted cheese"></div>
<div class="abs tri-down" style="left:335px;top:727px"></div>
<div class="abs tri-up" style="left:502px;top:718px"></div>
<article class="abs tasting tasting-b">
  <h4>BEST TASTING EVER</h4>
  <p>benign information that does not contain any usefubenign information that does not contain any usefu</p>
</article>
<article class="abs card offers">
  <div class="card-head">OFFERS</div>
  <p class="card-body">Dummy data is benign information that does not contain any useful data, but serves to re-serve space where real data is nominally pre-sent. Dummy data can be used as cholder for both not contain any useful data, but serves to reserve space where real data is nominally present. Dummy data can be used as cholder for both &nbsp;testing .</p>
</article>

<section class="abs story"></section>
<div class="abs story-divider"></div>
<div class="abs corner tl" style="left:132px;top:890px"></div>
<div class="abs produce" role="img" aria-label="Shopping bag filled with fresh vegetables"></div>
<div class="abs corner br" style="left:209px;top:997px"></div>
<div class="abs section-title" style="left:242px;top:897px">HOW CAN YOU CHANGE</div>
<p class="abs quote" style="left:241px;top:930px;width:215px">"We go to extraordinary lengths to provide world-class healthcare staffing and believe we can help achieve real improvements in patient care."</p>
<div class="abs link" style="left:381px;top:987px">WATCH DEMO</div>

<div class="abs corner tl" style="left:495px;top:909px"></div>
<div class="abs newsprint" role="img" aria-label="Folded newspaper"></div>
<div class="abs corner br" style="left:575px;top:976px"></div>
<div class="abs" style="left:598px;top:902px;font-family:'Open Sans',sans-serif;font-size:11px;color:var(--orange)">NEWS</div>
<div class="abs quote" style="left:602px;top:929px;width:80px;font-size:8px;line-height:11px">What's going on<br>in our world</div>
<div class="abs" style="left:637px;top:963px;font-family:'Open Sans',sans-serif;font-size:26px;color:var(--orange)">?</div>

<footer class="abs footer">
  <div class="abs foot-head" style="left:203px;top:40px">HOME</div>
  <ul class="abs foot-list" style="left:203px;top:56px"><li>ABOUT</li><li>SERVICES</li><li>CONTACT US</li></ul>
  <div class="abs foot-head" style="left:309px;top:40px">MENU</div>
  <p class="abs foot-text" style="left:309px;top:56px;width:152px">benign &nbsp;any useful data, but serves to reserve space enign &nbsp;any useful data, but serves to reserve space where real data is nominally......</p>
  <div class="abs foot-head" style="left:479px;top:40px">BRANCH</div>
  <svg class="abs" style="left:479px;top:55px" width="10" height="10" viewBox="0 0 10 10"><path d="M5 1a3 3 0 0 1 3 3c0 2.2-3 5-3 5S2 6.2 2 4a3 3 0 0 1 3-3z" fill="#222"/><circle cx="5" cy="4" r="1.1" fill="#efeeee"/></svg>
  <div class="abs foot-text" style="left:500px;top:57px">12 ridge lane ..hollow vale</div>
  <svg class="abs" style="left:479px;top:76px" width="10" height="10" viewBox="0 0 10 10"><path d="M5 1a3 3 0 0 1 3 3c0 2.2-3 5-3 5S2 6.2 2 4a3 3 0 0 1 3-3z" fill="#222"/><circle cx="5" cy="4" r="1.1" fill="#efeeee"/></svg>
  <p class="abs foot-text" style="left:500px;top:78px;width:100px">BRANCH2: Bayside 48 harbour road west.</p>
</footer>

<div class="abs bottom-bar">
  <div class="abs copyright">ALLRIGHTS RESERVED BY CORRIMBEL LODGE©2013 TERMS OF USE</div>
  <span class="abs social" style="left:709px;border:1px solid #fff"></span>
  <svg class="abs" style="left:726px;top:4px" width="10" height="10" viewBox="0 0 10 10"><path d="M1 5 5 1.5 9 5M2.5 4v5h5V4" fill="none" stroke="#fff" stroke-width="1.3"/></svg>
  <svg class="abs" style="left:746px;top:4px" width="10" height="10" viewBox="0 0 10 10"><circle cx="4" cy="4" r="2.7" fill="none" stroke="#fff" stroke-width="1.3"/><path d="M6 6l3 3" stroke="#fff" stroke-width="1.5"/></svg>
</div>
</body>
</html>
```